Recrutering company needs a Roll-Up Design

We need a Roll-Up Design for our company, which is dedicated to personnel selection. We would like the roll-up to feature our logo and the silhouette of the buildings shown in one of the uploaded photos (the one called "CorbelloVistaUrte4"). Additionally, we'd like to incorporate the words "Persones," "Talent," and "Èxit" with shadows using the English equivalents instead of the original ones, so: "People" for "Persones," "Talent" for "Talent," and "Success" for "Èxit."

The color of the logo can be changed to red, and the overall design can incorporate this color. As the design is for a roll-up, its essential to take into account a 4cm margin.

```html
<!DOCTYPE html>
<html lang="ca">
<head>
<meta charset="utf-8">
<title>Veltora — Roll-Up</title>
<link rel="stylesheet" href="https://fonts.googleapis.com/css2?family=Cinzel:wght@400&family=Montserrat:wght@500&family=Poppins:wght@800&display=swap">
<style>
  :root {
    --stage: #1f3346;
    --paper: #f4f4f4;
    --paper-shade: #dcdcdc;
    --ink: #2a2a2a;
    --night: #262626;
    --night-deep: #1b1b1b;
    --brand-red: #b5214a;
    --word-white: #ffffff;
    --echo-grey: #6a6869;
  }
  * { margin: 0; padding: 0; box-sizing: border-box; }
  html, body {
    width: 773px;
    height: 1200px;
    overflow: hidden;
    background: var(--stage);
  }
  .rollup {
    position: absolute;
    left: 151px;
    top: 20px;
    width: 471px;
    height: 1160px;
    overflow: hidden;
    background: linear-gradient(160deg, var(--paper) 0%, #ffffff 35%, var(--paper-shade) 100%);
  }
  .brand {
    position: absolute;
    top: 0;
    left: 0;
    width: 100%;
    text-align: center;
  }
  .brand-dot {
    position: absolute;
    top: 160px;
    left: 215px;
    width: 42px;
    height: 42px;
    border-radius: 50%;
    background: var(--brand-red);
  }
  .brand-name {
    position: absolute;
    top: 258px;
    left: 0;
    width: 100%;
    font-family: "Cinzel", serif;
    font-weight: 400;
    font-size: 76px;
    line-height: 1;
    letter-spacing: 2px;
    color: var(--ink);
  }
  .brand-tagline {
    position: absolute;
    top: 337px;
    left: 0;
    width: 100%;
    font-family: "Montserrat", sans-serif;
    font-weight: 500;
    font-size: 18px;
    letter-spacing: 6px;
    color: var(--brand-red);
  }
  .skyline {
    position: absolute;
    top: 391px;
    left: 0;
    width: 100%;
    height: 175px;
    background: linear-gradient(180deg, rgba(38,38,38,0) 0%, rgba(38,38,38,0.35) 55%, var(--night) 100%);
  }
  .night-panel {
    position: absolute;
    top: 560px;
    left: 0;
    width: 100%;
    height: 600px;
    background: linear-gradient(170deg, var(--night) 0%, #2e2e2e 50%, var(--night-deep) 100%);
  }
  .words {
    position: absolute;
    inset: 0;
    width: 471px;
    height: 1160px;
  }
  .word {
    font-family: "Poppins", sans-serif;
    font-weight: 800;
    fill: var(--word-white);
  }
  .echo {
    font-family: "Poppins", sans-serif;
    font-weight: 800;
  }
</style>
</head>
<body>
  <main class="rollup">
    <header class="brand">
      <span class="brand-dot"></span>
      <h1 class="brand-name">VELTORA</h1>
      <p class="brand-tagline">SELECCIÓ DE TALENT</p>
    </header>

    <div class="skyline" role="img" aria-label="Dark silhouette of town buildings and a factory chimney"></div>
    <div class="night-panel"></div>

    <svg class="words" viewBox="0 0 471 1160" aria-label="People, Talent, Success">
      <defs>
        <linearGradient id="echoFade" x1="0" y1="0" x2="0" y2="1">
          <stop offset="0" stop-color="#6a6869" stop-opacity="0.9"/>
          <stop offset="1" stop-color="#2a2a2a" stop-opacity="0"/>
        </linearGradient>
      </defs>

      <text class="echo" x="64" y="743" font-size="72" textLength="362" lengthAdjust="spacingAndGlyphs" fill="url(#echoFade)">PERSONES</text>
      <text class="word" x="52" y="687" font-size="108" textLength="374" lengthAdjust="spacingAndGlyphs">PEOPLE</text>

      <text class="echo" x="47" y="924" font-size="104" textLength="383" lengthAdjust="spacingAndGlyphs" fill="url(#echoFade)">TALENT</text>
      <text class="word" x="44" y="849" font-size="108" textLength="386" lengthAdjust="spacingAndGlyphs">TALENT</text>

      <text class="echo" x="62" y="1119" font-size="156" textLength="368" lengthAdjust="spacingAndGlyphs" fill="url(#echoFade)">EXIT</text>
      <text class="word" x="44" y="1006" font-size="90" textLength="383" lengthAdjust="spacingAndGlyphs">SUCCESS</text>
    </svg>
  </main>
</body>
</html>
```